Brennwald Metrics GmbH
Brennwald Metrics GmbH - Financial Services
Creative Brief
Professional
Lionel T Brennwald
Managing Director
Lindenweg 42 CH-6300 Zug Switzerland
U.S. Telephone 203.555.0186
lionel.brennwald@brennwaldmetrics-example.ch
brennwaldmetrics-example.ch
Wedsite will have partial moon crater stripped across the top. It might be interesting on the business card. Hard to tell if it will be too busy. JPG attached. Else simple is better. Note that address is broken after 19, and after Zug. It doesn't show on the confirmation. Kindly upload business cards and stationary, not just Business cards. It has to be a package

```html
<!DOCTYPE html>
<html lang="en">
<head>
<meta charset="utf-8">
<title>Brennwald Metrics GmbH – Stationery Package</title>
<link href="https://fonts.googleapis.com/css2?family=Lato:wght@400;700;900&display=swap" rel="stylesheet">
<style>
  :root {
    --bg: #e9e7e3;
    --paper: #ffffff;
    --navy: #1d3566;
    --blue: #2c5ba8;
    --sky: #6f93c9;
    --grey-text: #6b6f78;
    --rule: #c9ced8;
    --moon-tone: rgba(160,166,178,.7);
    --moon-soft: rgba(196,200,208,.45);
  }
  * { box-sizing: border-box; margin: 0; padding: 0; }
  html, body { width: 1200px; height: 547px; overflow: hidden; }
  body {
    background: var(--bg);
    font-family: "Lato", Arial, sans-serif;
    color: var(--navy);
    position: relative;
  }
  .sheet {
    position: absolute;
    background: var(--paper);
    overflow: hidden;
    box-shadow: 0 1px 3px rgba(0,0,0,.18);
  }
  .moon-area {
    position: absolute;
    background: radial-gradient(ellipse at 60% 60%, var(--moon-tone) 0%, var(--moon-soft) 40%, rgba(255,255,255,0) 70%);
  }
  .brand, .person, .letter, .fax-title, .fax-strip, .fax-form, .page-foot { z-index: 1; }
  .brand { display: flex; align-items: center; gap: 4px; white-space: nowrap; }
  .brand-square { background: var(--navy); flex: none; }
  .brand-name { font-weight: 900; color: var(--navy); letter-spacing: .06em; line-height: 1; }
  .brand-address {
    border-left: 1px solid var(--rule);
    color: var(--grey-text);
    line-height: 1.35;
  }
  .foot-band {
    position: absolute; left: 0; right: 0; bottom: 0;
    background: var(--blue);
    border-top: 2px solid var(--sky);
  }
  .foot-web {
    position: absolute; right: 0; bottom: 0;
    background: var(--navy); color: #fff;
    font-weight: 700; letter-spacing: .04em;
  }

  /* Business cards */
  .card-front { left: 29px; top: 29px; width: 134px; height: 74px; }
  .card-front .brand { position: absolute; left: 8px; top: 8px; }
  .card-front .brand-square { width: 7px; height: 7px; }
  .card-front .brand-name { font-size: 6px; }
  .card-front .person { position: absolute; left: 8px; top: 26px; font-size: 4px; color: var(--grey-text); line-height: 1.45; }
  .card-front .person strong { color: var(--navy); font-size: 5px; }
  .card-front .moon-area { width: 90px; height: 70px; right: -30px; bottom: -30px; }
  .card-back { left: 172px; top: 29px; width: 134px; height: 74px; background: linear-gradient(135deg, #d6d9de, #aab0b9); }
  .card-back .brand { position: absolute; left: 0; right: 0; top: 32px; justify-content: center; }
  .card-back .brand-square { width: 8px; height: 8px; }
  .card-back .brand-name { font-size: 7px; }

  /* Envelopes */
  .envelope-front { left: 12px; top: 150px; width: 379px; height: 190px; }
  .envelope-front .brand { position: absolute; left: 12px; top: 14px; gap: 6px; }
  .envelope-front .brand-square { width: 13px; height: 13px; }
  .envelope-front .brand-name { font-size: 10px; }
  .envelope-front .brand-address { font-size: 5px; padding-left: 6px; }
  .envelope-front .moon-area { width: 260px; height: 200px; right: -70px; bottom: -60px; }
  .envelope-front .foot-band { height: 6px; z-index: 1; }
  .envelope-back { left: 12px; top: 358px; width: 379px; height: 180px; }
  .envelope-back svg { position: absolute; inset: 0; }
  .envelope-back .brand { position: absolute; left: 150px; top: 32px; gap: 5px; }
  .envelope-back .brand-square { width: 11px; height: 11px; }
  .envelope-back .brand-name { font-size: 9px; }

  /* Letterhead & fax */
  .letterhead { left: 432px; top: 12px; width: 348px; height: 522px; }
  .fax { left: 821px; top: 12px; width: 350px; height: 522px; }
  .page-head { position: absolute; left: 18px; top: 16px; gap: 7px; }
  .page-head .brand-square { width: 15px; height: 15px; }
  .page-head .brand-name { font-size: 11px; }
  .page-head .brand-address { font-size: 5px; padding-left: 7px; }
  .page-moon { width: 280px; height: 240px; right: -80px; bottom: -50px; }
  .page-foot { position: absolute; left: 0; right: 0; bottom: 0; height: 12px; }
  .page-foot .foot-band { height: 10px; }
  .page-foot .foot-web { font-size: 5px; padding: 3px 8px; }

  .letter { position: absolute; left: 40px; top: 80px; width: 270px; font-size: 4.6px; line-height: 1.6; color: #444; }
  .letter p { margin-bottom: 7px; }

  .fax-title {
    position: absolute; right: 18px; top: 64px;
    display: flex; align-items: center; gap: 5px;
    font-weight: 900; font-size: 10px; color: var(--navy); letter-spacing: .1em;
  }
  .fax-strip { position: absolute; left: 18px; right: 18px; top: 82px; height: 3px; background: var(--blue); }
  .fax-form { position: absolute; left: 18px; right: 18px; top: 95px; }
  .fax-row { display: flex; align-items: center; height: 14px; margin-bottom: 4px; font-size: 5px; color: var(--grey-text); }
  .fax-row .tab { width: 26px; height: 14px; margin-right: 6px; }
  .fax-row .tab.filled { background: var(--navy); color: #fff; font-weight: 700; display: flex; align-items: center; justify-content: center; }
  .fax-row .label { width: 40px; text-align: right; padding-right: 6px; }
  .fax-row .field { flex: 1; height: 10px; border: 1px solid var(--rule); background: #f6f7f9; }
  .fax-row.gap { margin-top: 10px; }
  .fax-notes { margin-left: 78px; height: 70px; border: 1px solid var(--rule); background: #f6f7f9; }
</style>
</head>
<body>

  <section class="sheet card-front">
    <div class="moon-area" role="img" aria-label="Partial moon crater photograph"></div>
    <div class="brand"><span class="brand-square"></span><span class="brand-name">BRENNWALD METRICS</span></div>
    <div class="person">
      <strong>Lionel T Brennwald</strong><br>
      Managing Director<br>
      Lindenweg 42 CH-6300 Zug Switzerland<br>
      U.S. Telephone 203.555.0186<br>
      lionel.brennwald@brennwaldmetrics-example.ch
    </div>
  </section>

  <section class="sheet card-back" role="img" aria-label="Moon crater surface photograph as card background">
    <div class="brand"><span class="brand-square"></span><span class="brand-name">BRENNWALD METRICS</span></div>
  </section>

  <section class="sheet envelope-front">
    <div class="moon-area" role="img" aria-label="Partial moon crater photograph"></div>
    <div class="brand">
      <span class="brand-square"></span><span class="brand-name">BRENNWALD METRICS</span>
      <span class="brand-address">Lindenweg 42<br>CH-6300 Zug<br>Switzerland</span>
    </div>
    <div class="foot-band"></div>
  </section>

  <section class="sheet envelope-back">
    <svg width="379" height="180" viewBox="0 0 379 180">
      <path d="M0 0 L189.5 95 L379 0" fill="none" stroke="#cfd3da" stroke-width="1"/>
      <path d="M0 180 L150 90 M379 180 L229 90" fill="none" stroke="#e0e3e8" stroke-width="1"/>
    </svg>
    <div class="brand"><span class="brand-square"></span><span class="brand-name">BRENNWALD METRICS</span></div>
  </section>

  <section class="sheet letterhead">
    <div class="moon-area page-moon" role="img" aria-label="Partial moon crater photograph"></div>
    <div class="brand page-head">
      <span class="brand-square"></span><span class="brand-name">BRENNWALD METRICS</span>
      <span class="brand-address">Lindenweg 42 CH-6300 Zug Switzerland<br>U.S. Telephone 203.555.0186<br>brennwaldmetrics-example.ch</span>
    </div>
    <div class="letter">
      <p>12 March 2024</p>
      <p>Anton Keller<br>Seestrasse 8<br>8002 Zurich</p>
      <p>Dear Mr. Keller,</p>
      <p>Thank you for your interest in our quantitative research services. We have reviewed your portfolio objectives and prepared a summary of the models and reporting options that best fit your requirements for the coming year.</p>
      <p>Our team combines long term market data with disciplined risk analysis to deliver clear, timely insight. Each report is reviewed by a senior analyst before release and is available in print and digital formats.</p>
      <p>Please let us know a convenient time to discuss the proposal in more detail. We look forward to working with you.</p>
      <p>Sincerely,<br><br>Lionel T Brennwald</p>
    </div>
    <div class="page-foot"><div class="foot-band"></div><div class="foot-web">brennwaldmetrics-example.ch</div></div>
  </section>

  <section class="sheet fax">
    <div class="moon-area page-moon" role="img" aria-label="Partial moon crater photograph"></div>
    <div class="brand page-head">
      <span class="brand-square"></span><span class="brand-name">BRENNWALD METRICS</span>
      <span class="brand-address">Lindenweg 42 CH-6300 Zug Switzerland<br>U.S. Telephone 203.555.0186<br>brennwaldmetrics-example.ch</span>
    </div>
    <div class="fax-title">
      <svg width="16" height="10" viewBox="0 0 16 10"><path d="M0 3.5h10V0l6 5-6 5V6.5H0z" fill="var(--blue)"/></svg>
      FAX
    </div>
    <div class="fax-strip"></div>
    <div class="fax-form">
      <div class="fax-row"><span class="tab filled">To</span><span class="label">Name</span><span class="field"></span></div>
      <div class="fax-row"><span class="tab"></span><span class="label">Company</span><span class="field"></span></div>
      <div class="fax-row"><span class="tab"></span><span class="label">Fax</span><span class="field"></span></div>
      <div class="fax-row"><span class="tab"></span><span class="label">Phone</span><span class="field"></span></div>
      <div class="fax-row gap"><span class="tab filled">From</span><span class="label">Name</span><span class="field"></span></div>
      <div class="fax-row"><span class="tab"></span><span class="label">Phone</span><span class="field"></span></div>
      <div class="fax-row"><span class="tab"></span><span class="label">Pages</span><span class="field"></span></div>
      <div class="fax-row gap"><span class="tab filled">Re</span><span class="label"></span><span class="field"></span></div>
      <div class="fax-notes"></div>
    </div>
    <div class="page-foot"><div class="foot-band"></div><div class="foot-web">brennwaldmetrics-example.ch</div></div>
  </section>

</body>
</html>
```